Redesign our Product Box!

We have a product box for our pet supplement we are looking to redesign. Please use the photoshop file of the current design for the logo/info/dieline and the concept picture of a bag we would like to see included in the box design.

Ideally the background will be the green with white text, but we really want it to be fun and appealing to pet owners so do not be scared to show your vision.

```html
<!DOCTYPE html>
<html lang="en">
<head>
<meta charset="utf-8">
<title>Seabloom Marine Phytoplankton Powder – Box Panels</title>
<link rel="stylesheet" href="https://fonts.googleapis.com/css2?family=Fira+Sans+Extra+Condensed:wght@800&family=Cabin:wght@400&family=Roboto+Condensed:wght@300;400&family=Archivo+Black&family=Arimo:wght@400;700&family=Poppins:wght@800&display=swap">
<style>
  :root {
    --green: #15a548;
    --lime: #95c93d;
    --white: #ffffff;
    --cream: #f2ea8c;
    --orange: #f7a443;
    --ink: #111111;
  }
  * { box-sizing: border-box; margin: 0; padding: 0; }
  html, body { width: 1200px; height: 1036px; overflow: hidden; background: var(--white); }
  .canvas { position: relative; width: 1200px; height: 1036px; }

  .front { position: absolute; left: 0; top: 0; width: 576px; height: 1036px; background: var(--green); overflow: hidden; }
  .brand-band { position: absolute; left: 404px; top: 0; width: 172px; height: 1036px; background: var(--lime); }
  .back { position: absolute; left: 624px; top: 0; width: 576px; height: 1036px; background: var(--green); }
  .back-overlay { position: absolute; left: 624px; top: 0; width: 576px; height: 1036px; }

  .product-title {
    position: absolute; left: 42px; top: 190px; width: 360px;
    font-family: "Fira Sans Extra Condensed", sans-serif; font-weight: 800;
    font-size: 37px; line-height: 34px; color: var(--white); letter-spacing: -0.3px;
  }
  .product-tagline {
    position: absolute; left: 51px; top: 344px;
    font-family: "Cabin", sans-serif; font-size: 27px; line-height: 34px; color: var(--cream);
  }
  .pet-artwork {
    position: absolute; left: 28px; top: 450px; width: 400px; height: 555px;
    border-radius: 40px;
    background: linear-gradient(160deg, var(--orange) 0%, #f8c27f 45%, var(--white) 100%);
    opacity: 0.9;
  }
  .net-weight {
    position: absolute; left: 33px; top: 965px;
    font-family: Arimo, sans-serif; font-weight: 700; font-size: 31px; color: var(--white);
  }
  .brand-name {
    position: absolute; left: 490px; top: 545px;
    transform: translate(-50%, -50%) rotate(-90deg);
    font-family: "Poppins", sans-serif; font-weight: 800; font-size: 128px; line-height: 1;
    color: var(--white); white-space: nowrap; letter-spacing: -2px;
  }

  .back-copy {
    position: absolute; left: 41px; width: 596px; color: var(--white);
    font-family: "Roboto Condensed", sans-serif; font-weight: 300;
    transform: scaleX(0.83); transform-origin: left top;
  }
  .rule { position: absolute; left: 41px; width: 495px; height: 2px; background: var(--white); }
  .intro { top: 140px; font-size: 17.6px; line-height: 20.8px; }
  .intro p, .benefits p, .directions { text-align: justify; }
  .directions { top: 325px; font-size: 18.4px; line-height: 21px; }
  .treasure-head { top: 383px; font-size: 18.4px; line-height: 22px; }
  .benefits { top: 423px; font-size: 18.4px; line-height: 20.8px; }
  .benefits p + p { margin-top: 5px; }

  .facts-card { position: absolute; left: 752px; top: 586px; width: 320px; height: 196px; background: var(--white); color: var(--ink); font-family: Arimo, sans-serif; }
  .facts-table { position: absolute; left: 13px; top: 8px; width: 296px; border: 1.5px solid var(--ink); }
  .facts-title { font-family: "Archivo Black", sans-serif; font-size: 25px; text-align: center; line-height: 36px; border-bottom: 1.5px solid var(--ink); }
  .facts-row { display: flex; align-items: center; font-size: 11.5px; line-height: 13px; padding: 3px 12px; border-bottom: 1.5px solid var(--ink); }
  .facts-row .name { flex: 1; }
  .facts-row .amount { width: 58px; text-align: center; }
  .facts-row .dv { width: 50px; text-align: center; }
  .facts-head { height: 41px; }
  .facts-item { height: 35px; }
  .facts-note { font-size: 11.5px; padding: 2px 12px; line-height: 12px; }
  .facts-disclaimer { position: absolute; left: 12px; top: 144px; width: 297px; font-size: 9.6px; line-height: 11px; text-align: justify; font-family: "Roboto Condensed", sans-serif; }
  .facts-storage { position: absolute; right: 12px; top: 177px; font-size: 10px; font-family: "Roboto Condensed", sans-serif; }

  .distributor { top: 802px; font-size: 14.6px; line-height: 14.6px; }
  .contact { top: 876px; font-size: 14.6px; line-height: 14.6px; }
  .warnings { top: 932px; font-size: 14.6px; line-height: 12.8px; text-align: justify; }
</style>
</head>
<body>
<main class="canvas">
  <section class="front">
    <div class="brand-band"></div>
    <h1 class="product-title">100% Pure Marine Phytoplankton Powder</h1>
    <p class="product-tagline">Foundational Nutrition<br>&amp; Super-Antioxidant<br>For Dogs &amp; Cats</p>
    <div class="pet-artwork" role="img" aria-label="Illustration of orange paw prints with white dog and cat silhouettes sitting together"></div>
    <div class="net-weight">15g</div>
    <div class="brand-name">seabloom</div>
  </section>

  <section class="back">
    <div class="rule" style="top:130px"></div>
    <div class="back-copy intro">
      <p>Our premium phytoplankton powder is a extraordinary supplement.&nbsp; It infuses your pet’s body with pure, plant-based nutrients and potent antioxidants.</p>
      <p>Phytoplankton goes beyond ordinary supplements; it's a path to optimal health. In just a few weeks, your pet will experience a feeling of calm and strength, the kind of wellness our customers often say they've been seeking.</p>
      <p>Join those who have discovered the transformative power of phytoplankton. See the difference for yourself and understand why it's not just a supplement, but a revolution in pet health and vitality.</p>
    </div>
    <div class="rule" style="top:317px"></div>
    <p class="back-copy directions">Directions: For dogs &amp; cats 1/16tsp once per day.&nbsp; Administer orally. To be mixed into food. 1/16tsp = 1/2 the included scoop.</p>
    <div class="rule" style="top:372px"></div>
    <p class="back-copy treasure-head">Unlock Nature’s Nutrient Treasure:</p>
    <div class="back-copy benefits">
      <p>Phytoplankton is the foundation of life, It is the first plant in the entire food chain.</p>
      <p>Phytoplankton is a microscopic powerhouse. Your pet’s body absorbs billions of phytoplankton with every serving.</p>
      <p>Packed with the building blocks of life, phytoplankton addresses multiple aspects of your pet’s health in one simple supplement.</p>
    </div>
  </section>

  <section class="facts-card">
    <div class="facts-table">
      <div class="facts-title">Supplement Facts</div>
      <div class="facts-row facts-head">
        <span class="name">Serving Size: 1 Scoop/Day<br>Servings per Container: 30</span>
        <span class="amount">Amount<br>Per<br>Serving</span>
        <span class="dv">%DV</span>
      </div>
      <div class="facts-row facts-item">
        <span class="name">Microalgae Nannochloropsis<br>Gaditana</span>
        <span class="amount">500g</span>
        <span class="dv">N/A*</span>
      </div>
      <div class="facts-note">*Daily value not established.</div>
    </div>
    <p class="facts-disclaimer">These statements have not been evaluated by the Food and Drug Administrations.&nbsp; This products is not intended to diagnose, treat, cure or prevent any disease.</p>
    <p class="facts-storage">Store in a cool, dry place.</p>
  </section>

  <section class="back-overlay">
    <p class="back-copy distributor">Distributed By:<br>Marinova Pet Nutrition Inc.<br>482-6 Harbour Road, Riverview,<br>New Brunswick Canada E1B 4K7</p>
    <p class="back-copy contact">Customer Care: 1 800 555 0142<br>marinovapetnutrition.com</p>
    <p class="back-copy warnings">Warnings: Check with a qualified healthcare professional before using this product if you are pregnant, breastfeeding, or taking blood thinners. You should call your doctor for medical advice about serious adverse events. To report a serious adverse event or obtain product information contact:&nbsp; 1 800 555 0142</p>
  </section>
</main>
</body>
</html>
```